Tandel Marketing needs a new website design

We need a homepage and sub-page design for our new marketing consulting business based in Perth, Western Australia. www.tandelmarketing-example.com.au

About Us:

Tandel Marketing specialises in providing professional and result orientated marketing advice to small and medium sized business. We focus on client's overall marketing communication mix and analyse their current marketing activities and give advise where to invest their budget in the future.

We also function as marketing freelancers and can put the developed marketing plans and strategies into action.

Colour Suggestions based on newly designed logo:
orange, dark blue, black and white

The final design should reflect strategic solutions, success, trust & knowledge.

Please refer to attached documents:
Wireframe - for an indication of the sections needed on the site
Sitemap - as guidance how the content is arranged/interlinked
Services - overview of our marketing consulting service areas
Logo - use as guideline for colours and style

Industry websites that are different and that we like:

1. http://www.vorlinqa-example.com/index.htm
- like the simplicity of this site

2. http://www.plaxterwood-example.com/ - like the integration of the services into the header

3. http://www.gorumisa-example.com/
like the concept of the display of services - can you come up with something for us based on our overview of services

Target Market(s)

Marketing Managers & Business Owners (age 30-50) of small to medium sized businesses in Perth/ Western Australia

Industry/Entity Type

Marketing

Requirements
Must have
• - clean design and customised site
- all elements as specified in the wireframes document (provided a few options but open to suggestions and ideas
- looking for ideas to display our services as per overview page which can be integrated into each page of the website
Should not have
• don’t want a template looking site
please don't just copy our wireframes and make the site too boxy

```html
<!DOCTYPE html>
<html lang="en">
<head>
<meta charset="utf-8">
<title>Tandel Marketing</title>
<link rel="stylesheet" href="https://fonts.googleapis.com/css2?family=Arimo:wght@400;700&family=Ubuntu:wght@400;500&display=swap">
<style>
:root{
  --orange:#e89a00;
  --orange-dark:#d98c00;
  --orange-head:#f07d00;
  --orange-about:#cf6510;
  --note-light:#f7b63a;
  --note-dark:#eda020;
  --text:#333333;
  --text-soft:#444444;
  --link:#1a78d6;
  --white:#ffffff;
  --black:#000000;
  --hero-top:#ffffff;
  --hero-bottom:#e4e4e4;
}
*{margin:0;padding:0;box-sizing:border-box}
html,body{width:1200px;height:1200px;overflow:hidden;background:var(--white)}
body{font-family:"Ubuntu",sans-serif;color:var(--text);position:relative}
.page{position:relative;width:1200px;height:1200px;overflow:hidden}
.abs{position:absolute}

.brand{display:flex;align-items:center;gap:10px;font-family:"Ubuntu",sans-serif;font-weight:500;color:var(--orange-head);letter-spacing:.5px}
.brand-dot{border-radius:50%;background:var(--orange-head);flex:none}
.site-brand{left:113px;top:24px;font-size:30px}
.site-brand .brand-dot{width:46px;height:46px}

.main-nav{left:0;top:105px;width:1200px;height:46px;background:linear-gradient(var(--orange),var(--orange-dark));border-top:1px solid #f2b23a}
.main-nav a{position:absolute;top:13px;color:var(--white);text-decoration:none;font-size:15px}

.hero{left:0;top:151px;width:1200px;height:292px;background:linear-gradient(var(--hero-top),var(--hero-bottom))}
.hero-photo{left:109px;top:13px;width:295px;height:276px;background:linear-gradient(160deg,#f3f3f3,#d8d8d8 55%,#3a3a3a)}
.hero-title{left:424px;top:38px;font-family:"Arimo",sans-serif;font-size:24px;color:var(--orange-head);font-weight:400}
.hero-text{left:424px;top:74px;width:660px;font-size:13px;line-height:22px;color:var(--text-soft);text-align:justify}
.call-button{left:800px;top:195px;width:284px;height:55px;border:1px solid #8fa0a8;background:var(--white);font-size:26px;color:#333;display:flex;align-items:center;justify-content:center}

.about-title{left:111px;top:469px;font-family:"Arimo",sans-serif;font-size:23px;color:var(--orange-about);font-weight:400}
.about-text{font-size:13px;line-height:22px;color:var(--text);text-align:justify}
.about-text.first{left:111px;top:507px;width:422px}
.about-text.second{left:111px;top:649px;width:653px}
.about-chart{left:548px;top:512px;width:216px;height:126px;border:3px solid #e2e2e2;background:var(--white)}
.view-more{left:112px;top:747px;font-size:13px;color:var(--link);text-decoration:none}

.note{width:290px;height:139px;background:linear-gradient(135deg,var(--note-light),var(--note-dark));box-shadow:-6px 6px 10px rgba(0,0,0,.25)}
.note h3{position:absolute;left:12px;top:16px;font-family:"Ubuntu",sans-serif;font-size:19px;font-weight:500;color:#1a1a1a}
.news-note{left:812px;top:479px}
.clients-note{left:812px;top:641px;height:137px}
.news-heading{position:absolute;left:12px;top:49px;font-size:13px;color:#7a2d00;text-decoration:underline}
.news-text{position:absolute;left:14px;top:69px;width:262px;font-size:11.5px;line-height:14px;color:#3a1a00}

.service{width:148px}
.service h4{font-family:"Arimo",sans-serif;font-size:14px;font-weight:700;line-height:17px;color:#222}
.service p{font-family:"Arimo",sans-serif;font-size:13px;line-height:18px;color:#333;text-align:justify;margin-top:var(--gap)}
.service-more{top:987px;font-family:"Arimo",sans-serif;font-size:13px;color:var(--link);text-decoration:underline}

.site-footer{left:0;top:1035px;width:1200px;height:165px;background:var(--black)}
.footer-col{top:16px;font-family:"Arimo",sans-serif;font-size:14px}
.footer-col h5{font-weight:400;color:var(--orange);font-size:14px;margin-bottom:8px}
.footer-col li{list-style:none;color:var(--white);line-height:24px}
.footer-brand{left:918px;top:22px;font-size:26px}
.footer-brand .brand-dot{width:40px;height:40px}
.copyright{right:115px;top:75px;font-family:"Arimo",sans-serif;font-size:13px;color:#c06a10}
</style>
</head>
<body>
<div class="page">
  <div class="abs brand site-brand"><span class="brand-dot"></span>Tandel Marketing</div>

  <nav class="abs main-nav">
    <a style="left:120px">Home</a>
    <a style="left:196px">Who We Are</a>
    <a style="left:321px">What We Do</a>
    <a style="left:448px">Ways We Innowate</a>
    <a style="left:616px">News</a>
    <a style="left:688px">Contact us</a>
  </nav>

  <section class="abs hero">
    <div class="abs hero-photo" role="img" aria-label="Photo of a smiling businesswoman holding a folder and making an OK gesture"></div>
    <h1 class="abs hero-title">IT ALL COMES DOWN TO TANDEL</h1>
    <p class="abs hero-text">At Tandel Marketing, we focus on your overall marketing communication mix and provide marketing solutions that will get you results. As part of our consulting process we provide you with realistic marketing strategies, plans and budgets incorporating a range of marketing services tailored to your business. We also function as a full service agency and can put your developed plans into action.</p>
    <div class="abs call-button">Call Us Now</div>
  </section>

  <h2 class="abs about-title">About us</h2>
  <p class="abs about-text first">At Tandel Marketing, we focus on your overall marketing communication mix and provide marketing solutions that will get you results. As part of our consulting process we provide you with realistic marketing strategies, plans and budgets incorporating a range of marketing services tailored to your business. We also function as a full service agency and can put your developed plans into action.</p>
  <div class="abs about-chart">
    <svg width="210" height="120" viewBox="0 0 210 120" role="img" aria-label="Rising bar chart with trend arrow">
      <g fill="#ececec" stroke="#d0d0d0">
        <rect x="8" y="58" width="18" height="52"/>
        <rect x="28" y="48" width="18" height="62"/>
        <rect x="48" y="58" width="18" height="52"/>
        <rect x="68" y="40" width="18" height="70"/>
        <rect x="88" y="28" width="18" height="82"/>
        <rect x="108" y="36" width="18" height="74"/>
        <rect x="128" y="22" width="18" height="88"/>
      </g>
      <polyline points="6,78 30,64 52,70 72,56 94,58 114,48 150,10" fill="none" stroke="#f08a00" stroke-width="3"/>
      <polygon points="156,4 144,10 152,17" fill="#f08a00"/>
      <line x1="2" y1="111" x2="205" y2="111" stroke="#cfcfcf"/>
    </svg>
  </div>
  <p class="abs about-text second">At Tandel Marketing, we focus on your overall marketing communication mix and provide marketing solutions that will get you results. As part of our consulting process we provide you with realistic marketing strategies, plans and budgets incorporating a range of marketing services tailored to your business. We also function as a full service agency and can put your developed plans into action.</p>
  <a class="abs view-more">View More &gt;</a>

  <aside class="abs note news-note">
    <h3>News</h3>
    <span class="news-heading">NewsHeading</span>
    <p class="news-text">Lorem Ipsum is simply dummy text of the printing and typesetting industry. Lorem Ipsum has been the industry's</p>
  </aside>
  <aside class="abs note clients-note">
    <h3>Clients</h3>
  </aside>

  <div class="abs service" style="left:100px;top:837px;--gap:18px">
    <h4>Cunsultant &amp; Strategy</h4>
    <p>Lorem ipsum dolor sit amet, cons ectetur adipiscing elit. Aliqu am</p>
  </div>
  <div class="abs service" style="left:279px;top:837px;--gap:18px">
    <h4>Marketing Managment</h4>
    <p>Lorem c ons cons adipiscing elit. cons ectetur adiectetur adipis cing elit.</p>
  </div>
  <div class="abs service" style="left:457px;top:837px;--gap:18px">
    <h4>Online Marketing</h4>
    <p>adipiscing elit. cons ectetur adi .lorem ipsum dolar sit a,et lorem sipsum lorem sita mater</p>
  </div>
  <div class="abs service" style="left:641px;top:837px;--gap:18px">
    <h4>Brand Marketing</h4>
    <p>dolar sir amet sit lorem porem lore ipsum se met setsum dolar sir am</p>
  </div>
  <div class="abs service" style="left:804px;top:837px;width:124px;--gap:18px">
    <h4>Event Management</h4>
    <p>Lorem ipsum dolor sit amet, cons ectetur adipiscing elit. Aliqu am</p>
  </div>
  <div class="abs service" style="left:960px;top:837px;width:124px;--gap:18px">
    <h4>Print Marketing</h4>
    <p>Lorem ipsum dolor sit amet, cons ectetur adipiscing elit. Aliqu am</p>
  </div>

  <a class="abs service-more" style="left:100px">More &gt;</a>
  <a class="abs service-more" style="left:279px">More &gt;</a>
  <a class="abs service-more" style="left:457px">More &gt;</a>
  <a class="abs service-more" style="left:641px">More &gt;</a>
  <a class="abs service-more" style="left:804px">More &gt;</a>
  <a class="abs service-more" style="left:960px">More &gt;</a>

  <footer class="abs site-footer">
    <div class="abs footer-col" style="left:118px">
      <h5>ABOUT US</h5>
      <ul><li>Information</li><li>Cunsulatant &amp; Strategy</li><li>Marketing Managment</li></ul>
    </div>
    <div class="abs footer-col" style="left:300px">
      <h5>CONTACT US</h5>
      <ul><li>Contact info</li><li>Address</li><li>Contact Form</li></ul>
    </div>
    <div class="abs footer-col" style="left:450px">
      <h5>PRIVACY</h5>
      <ul><li>Terms &amp; Conditions</li><li>Privacy Statement</li><li>FAQ's</li></ul>
    </div>
    <div class="abs brand footer-brand"><span class="brand-dot"></span>Tandel</div>
    <p class="abs copyright">© All Right Reserved 2012 www.tandelmarketing-example.com.au</p>
  </footer>
</div>
</body>
</html>
```